Newspaper ad advertising bathroom adaptations for the less-abled and disabled.

This ad is to really promote bathroom adaptations that are suited to the clients needs, so more care led rather than design led. Important for the ad to be easy to read and easy to understand. Clearly states bathroom conversions from £4,999 to help qualify leads generated from the ad. We are looking to reach out to anyone whose bathroom is becoming more challenging because of mobility issues so we can use our excellent industry knowledge and personal family experience to come up with solutions that really work for the client

Target Market(s)

predominately older people

Industry/Entity Type

Health And Wellness

Font styles to use
Serif

Colors

Designer to choose colors to be used in the design.

Requirements
Must have
• It must have the content that is included in advert i have attached. Use where possible the photos of the actual jobs we've done to make it relatable for the client to see real jobs.
Nice to have
• some added pictures of mobility bathroom equipment including walk-in baths, walk-in showers and wetroom flooring.
Should not have
• anything too heavy on the eye.

```html
<!DOCTYPE html>
<html lang="en">
<head>
<meta charset="utf-8">
<title>Harbour Adaptations – Bathroom Adaptations Advert</title>
<link href="https://fonts.googleapis.com/css2?family=Tinos:ital,wght@0,400;0,700;1,700&family=Montserrat:wght@600;700&family=Arimo:wght@400&display=swap" rel="stylesheet">
<style>
  :root {
    --teal: #00a6a0;
    --orange: #f37021;
    --navy: #1b4583;
    --white: #ffffff;
    --ink: #1f2a36;
    --grey-text: #4a4f55;
    --panel: #ececec;
  }
  * { margin: 0; padding: 0; box-sizing: border-box; }
  html, body { width: 855px; height: 1200px; overflow: hidden; background: var(--white); }
  .advert { position: relative; width: 855px; height: 1200px; overflow: hidden; background: var(--white); font-family: "Tinos", "Times New Roman", serif; color: var(--ink); }
  .abs { position: absolute; white-space: nowrap; }

  .hero-band { position: absolute; left: 0; top: 0; width: 855px; height: 671px; background: var(--teal); }

  .brand { left: 514px; top: 60px; display: flex; align-items: center; gap: 10px; }
  .brand-dot { width: 30px; height: 30px; border-radius: 50%; background: var(--white); }
  .brand-name { font-family: "Montserrat", sans-serif; font-weight: 700; font-size: 20px; color: var(--white); }
  .web-address { left: 518px; top: 126px; font-family: "Montserrat", sans-serif; font-weight: 700; font-size: 18px; color: var(--white); letter-spacing: 0.3px; }

  .headline { left: 65px; color: var(--white); font-weight: 700; }
  .headline-q { font-size: 40px; line-height: 1; }
  .headline-q.line-1 { top: 174px; }
  .headline-q.line-2 { top: 222px; }
  .headline-answer { top: 268px; font-size: 59px; line-height: 1; }

  .dotted-rule { position: absolute; left: 46px; width: 729px; border-top: 1.5px dotted rgba(255,255,255,0.8); }
  .dotted-rule.upper { top: 342px; }
  .dotted-rule.lower { top: 395px; }

  .subhead { left: 65px; top: 355px; font-size: 27px; font-weight: 700; color: var(--white); }
  .tagline { left: 65px; top: 409px; font-size: 19.7px; font-weight: 700; font-style: italic; color: var(--white); }

  .photo { position: absolute; border: 1px solid #ffffff; border-radius: 8px; }
  .photo-main { left: 49px; top: 470px; width: 406px; height: 333px; border-radius: 12px; background: linear-gradient(160deg, #f2f2f0 0%, #dcdedd 45%, #8d9592 100%); }
  .photo-shower-chair { left: 310px; top: 609px; width: 165px; height: 166px; background: linear-gradient(170deg, #dadcdc 0%, #c4c7c8 60%, #9aa09d 100%); }
  .photo-walkin-shower { left: 483px; top: 609px; width: 144px; height: 166px; background: linear-gradient(170deg, #9ea3a6 0%, #7d8387 55%, #5d6367 100%); }
  .photo-seat { left: 636px; top: 609px; width: 158px; height: 166px; background: linear-gradient(170deg, #e6e8e8 0%, #d2d5d6 60%, #b9bec0 100%); }

  .price-outline { position: absolute; left: 302px; top: 512px; width: 504px; height: 74px; border: 1.5px solid var(--white); border-radius: 8px; }
  .price-box { position: absolute; left: 313px; top: 503px; width: 482px; height: 92px; background: var(--orange); border-radius: 10px; box-shadow: 0 3px 6px rgba(0,0,0,0.25); display: flex; flex-direction: column; justify-content: center; align-items: center; color: var(--white); font-weight: 700; font-size: 24.5px; line-height: 1.15; letter-spacing: 0.4px; text-align: center; }

  .quote { left: 476px; top: 789px; font-size: 14px; font-style: italic; font-weight: 700; color: var(--grey-text); }

  .features { position: absolute; left: 47px; top: 829px; width: 761px; height: 179px; border: 1.5px dotted var(--teal); border-radius: 8px; }
  .feature-list { position: absolute; list-style: none; font-size: 13.6px; font-weight: 700; color: var(--ink); line-height: 19.3px; }
  .feature-list.left { left: 42px; top: 9px; }
  .feature-list.right { left: 424px; top: 9px; }
  .feature-list li { position: relative; padding-left: 14px; white-space: nowrap; }
  .feature-list li::before { content: ""; position: absolute; left: 0; top: 6px; width: 6px; height: 6px; background: var(--teal); transform: rotate(45deg); }
  .feature-list li.wrap { line-height: 15px; margin-top: 2px; }

  .accreditations { position: absolute; left: 49px; top: 1067px; width: 337px; height: 59px; background: var(--panel); border-radius: 6px; display: flex; align-items: center; gap: 14px; padding-left: 14px; }
  .badge { background: #d2d2d2; }
  .badge.rect { width: 56px; height: 40px; border-radius: 3px; }
  .badge.wide { width: 64px; height: 20px; border-radius: 3px; }
  .badge.circle { width: 38px; height: 38px; border-radius: 50%; }

  .cta { position: absolute; left: 447px; top: 1034px; width: 358px; display: flex; flex-direction: column; align-items: center; font-size: 17px; font-weight: 700; color: var(--grey-text); line-height: 19px; letter-spacing: -0.2px; }
  .cta span { white-space: nowrap; }
  .phone { left: 455px; top: 1078px; display: flex; align-items: center; gap: 8px; }
  .phone-number { font-size: 50px; font-weight: 700; color: var(--orange); line-height: 1; }
  .email { left: 452px; top: 1130px; font-family: "Montserrat", sans-serif; font-weight: 600; font-size: 15.8px; color: var(--ink); }

  .footer-band { position: absolute; left: 0; top: 1171px; width: 855px; height: 29px; background: var(--navy); }
  .footnote { right: 51px; top: 1180px; font-family: "Arimo", sans-serif; font-size: 9px; color: var(--white); }
</style>
</head>
<body>
<main class="advert">
  <div class="hero-band"></div>

  <div class="abs brand">
    <span class="brand-dot"></span>
    <span class="brand-name">Harbour Adaptations</span>
  </div>
  <div class="abs web-address">www.harbouradaptations.com</div>

  <h1>
    <span class="abs headline headline-q line-1">Is your bathroom becoming</span>
    <span class="abs headline headline-q line-2">more challenging?</span>
    <span class="abs headline headline-answer">We have the solution...</span>
  </h1>

  <div class="dotted-rule upper"></div>
  <h2 class="abs subhead">Bathroom adaptations for the elderly, disabled and less abled</h2>
  <div class="dotted-rule lower"></div>
  <p class="abs tagline">we care passionately about installing a quality bathroom that really works for your needs</p>

  <div class="photo photo-main" role="img" aria-label="Completed adapted bathroom with toilet, fold-down grab rail, basin and shower area"></div>
  <div class="price-outline"></div>
  <div class="price-box">
    <span>Adapted bathroom conversions to help</span>
    <span>with your mobility needs from £4,999*</span>
  </div>
  <div class="photo photo-shower-chair" role="img" aria-label="Shower with grab rail and white shower chair"></div>
  <div class="photo photo-walkin-shower" role="img" aria-label="Walk-in shower with grey wall panelling and glass screen"></div>
  <div class="photo photo-seat" role="img" aria-label="Wetroom with shower seat and hand shower"></div>

  <p class="abs quote">“From concept to creation to completion...we do it all”</p>

  <section class="features">
    <ul class="feature-list left">
      <li>Existing bathroom to wetroom conversions</li>
      <li>Walk-in showers &amp; wetrooms tailored to meet your needs</li>
      <li>Full bathroom mobility enablement</li>
      <li>Free no obligation home assessment</li>
      <li>Full detailed pre-install survey</li>
      <li>Fully project managed dedicated installation team</li>
      <li>Full insurance backed guarantee on all adaptations</li>
      <li>All tiling, Electrics, Plumbing etc carried out</li>
    </ul>
    <ul class="feature-list right">
      <li>Bathing enabling equipment</li>
      <li>Work closely with occupational therapists</li>
      <li>Anti-slip safety flooring</li>
      <li>Maintenance free shower panelling</li>
      <li>Walk-in easy access baths</li>
      <li>Specialist wash &amp; dry toilets</li>
      <li class="wrap">Fully accredited to Fair Trader Guide, Homecare<br>Trades Guild and Consumer Fair Trading Council</li>
    </ul>
  </section>

  <div class="accreditations" aria-label="Accreditation badges">
    <span class="badge rect"></span>
    <span class="badge wide"></span>
    <span class="badge rect"></span>
    <span class="badge circle"></span>
    <span class="badge circle"></span>
  </div>

  <p class="cta">
    <span>CALL TODAY FOR A NO OBLIGATION</span>
    <span>HOME ASSESSMENT OR A BROCHURE</span>
  </p>
  <div class="abs phone">
    <svg width="32" height="32" viewBox="0 0 32 32" aria-hidden="true">
      <circle cx="16" cy="16" r="14" fill="none" stroke="#f37021" stroke-width="3"/>
      <path d="M11 9c1-1 2-1 3 0l2 3c.5 1 0 2-1 2.5-.5.3-.5 1 0 2l1.5 1.5c1 .8 1.6.8 2 0 .6-1 1.6-1.5 2.5-1l3 2c1 1 1 2 0 3-2 2-5 2-8 0-3-2-5-4-7-7-2-3-1-5 2-6z" fill="#f37021"/>
    </svg>
    <span class="phone-number">01632 960 418</span>
  </div>
  <p class="abs email">Email: enquiries@harbouradaptations.com</p>

  <div class="footer-band"></div>
  <p class="abs footnote">*Pricing is a guide only and could vary dependant on home survey and work involved</p>
</main>
</body>
</html>
```